Professional website for psychological services

Create a professional, easy to navigate website using soothing coastal images and incorporate company logo in design. Website is for a small private clinic that provides psychological services and must be appealing to professional men and women. A website I really like is www.veltoriparc.com I would love something like similar.

Target Market(s)

Professional men and women seeking psychological services

Industry/Entity Type

Mental Health

Number of Pages Required

5+ page

Requirements
Must have
• The website must incorporate the logo provided. The name of the company/website is Brimwell Harbor Renewal Aftercare. Colors must compliment the logo, must be coastal and soothing yet very professional. I would like a website like www.veltoriparc.com
• Pages will be:Home, Services, FAQ and Contact Us. The images included of the building and office are for the contact us page. Under the tab Servies: Individual Psychotherapy, Family Therapy, EMDR I will provide specific content for each.
Nice to have
• I want the website to be easy to navigate and the font easy to read. The writing on the logo is very light and I'm open to changing it slightly if it will be better aesthetically.
Should not have
• Please no pictures of any swimsuits, alcoholic beverages, etc. This is a professional psychological clinic.

```html
<!DOCTYPE html>
<html lang="en">
<head>
<meta charset="utf-8">
<title>Brimwell Harbor Renewal Aftercare</title>
<link rel="stylesheet" href="https://fonts.googleapis.com/css2?family=Noto+Serif:ital,wght@0,400;0,700;1,400;1,700&family=Open+Sans:wght@400;600;700&display=swap">
<style>
:root{
  --teal:#2bbbd6;
  --teal-deep:#1ea9c4;
  --ink:#111;
  --body:#333;
  --muted:#777;
  --paper:#fff;
  --mist:#f6f6f6;
  --line:#dcdcdc;
  --sand:#d9b38c;
}
*{box-sizing:border-box;margin:0;padding:0}
html,body{width:1200px;height:2311px;overflow:hidden}
body{background:var(--paper);color:var(--body);font-family:"Open Sans",Arial,sans-serif;position:relative}
.serif{font-family:"Noto Serif",Georgia,serif}
.abs{position:absolute}

/* header */
.brand{left:0;width:1200px;top:30px;text-align:center}
.brand-mark{width:34px;height:34px;border-radius:50%;background:var(--teal);margin:0 auto 10px}
.brand-name{font-family:"Noto Serif",Georgia,serif;color:var(--teal);font-size:30px;line-height:1.1}
.brand-rule{width:60px;height:1px;background:var(--line);margin:8px auto 5px}
.brand-tag{font-size:8px;letter-spacing:2px;color:var(--sand);text-transform:uppercase}
.nav{top:161px;left:0;width:1200px;display:flex;justify-content:center;gap:22px}
.nav a{font-size:9.5px;font-weight:600;color:var(--ink);text-decoration:none;text-transform:uppercase;padding:5px 16px;border-radius:14px;border:1.5px solid transparent}
.nav a.active{border-color:var(--teal)}

/* hero */
.hero{top:205px;left:0;width:1200px;height:460px;background:linear-gradient(90deg,#bfe4f3 0%,#d9eef7 35%,#a9d6ea 60%,#cfe8f3 100%)}
.hero-title{left:610px;top:392px;font-family:"Noto Serif",Georgia,serif;font-weight:700;font-size:18px;color:var(--ink);letter-spacing:.3px}
.hero-quote{left:610px;top:430px;width:590px;height:123px;background:rgba(255,255,255,.6);padding:16px 22px}
.hero-quote p{font-family:"Noto Serif",Georgia,serif;font-style:italic;font-size:14px;line-height:1.25;color:var(--ink);width:520px}
.hero-quote .sign{position:absolute;right:90px;bottom:14px;font-family:"Noto Serif",Georgia,serif;font-size:16px;color:var(--ink)}
.dots{left:930px;top:630px;display:flex;gap:4px}
.dots i{width:7px;height:7px;border-radius:50%;border:1px solid #fff;background:transparent;display:block}
.dots i.on{background:var(--teal);border-color:var(--teal)}

/* services strip */
.strip{top:665px;left:0;width:1200px;height:267px;background:var(--mist)}
.strip-photo{top:665px;left:0;width:404px;height:267px;background:linear-gradient(135deg,#3cc2da,#2bb3cf)}
.strip-frame{left:25px;top:693px;width:352px;height:213px;border:5px solid #fff;padding:46px 30px 0 33px;color:#fff}
.strip-frame h3{font-family:"Noto Serif",Georgia,serif;font-size:18px;font-weight:700;line-height:1.2;margin-bottom:8px}
.strip-frame p{font-size:8.5px;line-height:1.55}
.service{top:748px;width:176px}
.service h4{font-family:"Noto Serif",Georgia,serif;font-size:13px;font-weight:700;color:var(--ink);margin-bottom:10px}
.service p{font-size:8.5px;line-height:1.75;color:var(--body);margin-bottom:10px}
.service a{font-size:8.5px;color:var(--teal);text-decoration:none;display:flex;align-items:center;gap:5px}

/* doctor */
.doctor{top:932px;left:0;width:1200px;height:337px;background:#f3f3f3}
.doctor-photo{top:932px;left:638px;width:562px;height:337px;background:linear-gradient(90deg,#f3f3f3 0%,#7ccfe2 18%,#3ab6d2 60%,#2ea9c6 100%)}
.doctor-copy{left:234px;top:965px;width:380px;color:var(--ink)}
.doctor-copy .hi{font-family:"Noto Serif",Georgia,serif;font-size:17px}
.doctor-copy h2{font-family:"Noto Serif",Georgia,serif;font-size:25px;font-weight:700;margin:3px 0 10px}
.doctor-copy .who{font-family:"Noto Serif",Georgia,serif;font-size:17px;margin-bottom:12px}
.doctor-copy .who b{font-weight:700}
.doctor-copy .who small{font-size:11px}
.doctor-copy p{font-size:8.5px;line-height:1.75;color:var(--body);margin-bottom:14px}
.doctor-copy .dial{font-family:"Noto Serif",Georgia,serif;font-size:18px;font-weight:700;margin-bottom:12px}
.btn{display:inline-block;background:var(--teal);color:#fff;font-size:8.5px;font-weight:700;text-transform:uppercase;text-align:center}
.btn-appt{width:140px;height:31px;line-height:31px}

/* contact */
.contact-head{top:1310px;left:0;width:1200px;text-align:center;color:var(--ink)}
.contact-head h2{font-family:"Noto Serif",Georgia,serif;font-size:26px;font-weight:700}
.contact-head p{font-family:"Noto Serif",Georgia,serif;font-size:13px;margin-top:2px}
.field{height:32px;border:1px solid var(--line);border-radius:2px;background:#fff;font-size:8.5px;color:#555;padding:0 10px;line-height:30px}
.field.area{height:108px;line-height:1;padding-top:12px}
.btn-send{left:565px;top:1608px;width:68px;height:25px;line-height:25px}

/* testimonial */
.testi{top:1685px;left:0;width:1200px;height:291px;background:linear-gradient(90deg,#35bcd6,#2bbbd6 40%,#2bbbd6)}
.quote-mark{left:232px;top:1808px}
.testi-text{left:234px;top:1848px;width:432px;font-size:9.5px;line-height:1.85;color:#fff}
.testi-dots{left:232px;top:1945px;display:flex;gap:6px}
.testi-dots i{display:block;width:16px;height:3px;background:rgba(255,255,255,.55)}
.testi-dots i.on{width:24px;background:#fff}
.testi-photo{left:698px;top:1748px;width:215px;height:279px;background:linear-gradient(180deg,#e9eef0,#cfd9dd 60%,#f2f2f2)}
.testi-name{left:479px;top:1992px;width:200px;text-align:right;font-family:"Noto Serif",Georgia,serif;font-style:italic;font-weight:700;font-size:18px;color:var(--teal)}
.testi-role{left:479px;top:2016px;width:200px;text-align:right;font-family:"Noto Serif",Georgia,serif;font-style:italic;font-size:9px;color:var(--ink)}

/* footer */
.foot-brand{left:0;width:1200px;top:2100px;text-align:center}
.foot-brand .brand-mark{width:20px;height:20px;margin-bottom:6px}
.foot-brand .brand-name{font-size:19px}
.foot-brand .brand-rule{width:40px;margin:5px auto 3px}
.foot-brand .brand-tag{font-size:6px}
.social{top:2182px;left:0;width:1200px;display:flex;justify-content:center;gap:8px}
.social i{display:block;width:35px;height:35px;border-radius:50%;background:#e3e3e3}
.copy{top:2243px;left:0;width:1200px;text-align:center;font-size:8.5px;color:var(--ink)}
</style>
</head>
<body>

<header>
  <div class="abs brand">
    <div class="brand-mark"></div>
    <div class="brand-name">Brimwell Harbor</div>
    <div class="brand-rule"></div>
    <div class="brand-tag">Renewal Aftercare</div>
  </div>
  <nav class="abs nav">
    <a class="active">Home</a><a>Services</a><a>FAQ</a><a>Contact Us</a>
  </nav>
</header>

<section>
  <div class="abs hero" role="img" aria-label="Portrait of a professional woman in a bright, glass-walled office"></div>
  <h1 class="abs hero-title">RECOVERY AFTERCARE</h1>
  <div class="abs hero-quote">
    <p>“Lorem ipsum dolor sit amet, consectetur adipiscing elit. Nunc pretium nulla eget enim vulputate iaculis. Donec et lacus ac elit.”</p>
    <span class="sign">– Brimwell Harbor</span>
  </div>
  <div class="abs dots"><i class="on"></i><i></i><i></i></div>
</section>

<section>
  <div class="abs strip"></div>
  <div class="abs strip-photo" role="img" aria-label="Therapist in session with a client, tinted blue"></div>
  <div class="abs strip-frame">
    <h3>Try to solve<br>some problems.</h3>
    <p>Sed sit amet purus metus. In aliquam lacinia hendrerit. Donec pretium nisi non ullamcorper aliquam. Etiam ultrices eget libero in aliquam. Etiam posuere odio et sapien finibus hendrerit.</p>
  </div>
  <div class="abs service" style="left:422px">
    <h4>Individual Psychotherapy</h4>
    <p>Lorem ipsum dolor sit amet, consectetur adipiscing elit. Nunc pretium nulla eget enim vulputate iaculis.</p>
    <a>Learn More <svg width="9" height="7" viewBox="0 0 9 7"><path d="M0 2h5V0l4 3.5L5 7V5H0z" fill="#2bbbd6"/></svg></a>
  </div>
  <div class="abs service" style="left:610px">
    <h4>Family Therapy</h4>
    <p>Lorem ipsum dolor sit amet, consectetur adipiscing elit. Nunc pretium nulla eget enim vulputate iaculis.</p>
    <a>Learn More <svg width="9" height="7" viewBox="0 0 9 7"><path d="M0 2h5V0l4 3.5L5 7V5H0z" fill="#2bbbd6"/></svg></a>
  </div>
  <div class="abs service" style="left:796px">
    <h4>EMDR</h4>
    <p>Lorem ipsum dolor sit amet, consectetur adipiscing elit. Nunc pretium nulla eget enim vulputate iaculis.</p>
    <a>Learn More <svg width="9" height="7" viewBox="0 0 9 7"><path d="M0 2h5V0l4 3.5L5 7V5H0z" fill="#2bbbd6"/></svg></a>
  </div>
</section>

<section>
  <div class="abs doctor"></div>
  <div class="abs doctor-photo" role="img" aria-label="Smiling psychiatrist in a dark blazer, blue-tinted street background"></div>
  <div class="abs doctor-copy">
    <div class="hi">Hi! do you need</div>
    <h2>Psychological Support ?</h2>
    <div class="who">I’m Doctor <b>Brimwell Harbor</b>, <small>psychiatrist</small></div>
    <p>Sed sit amet purus metus. In aliquam lacinia hendrerit. Donec pretium nisi non ullamcorper aliquam. Etiam ultrices eget libero in aliquam. Etiam posuere odio et sapien finibus hendrerit. Curabitur porta vitae augue ut euismod. Suspendisse vel ex quis urna convallis pretium. Nulla ante neque, lobortis sed gravida id, fringilla tincidunt nisi. Vestibulum blandit mi ac dui dignissim varius.</p>
    <div class="dial">Just Dial +1098765432</div>
    <span class="btn btn-appt">Make an Appointment</span>
  </div>
</section>

<section>
  <div class="abs contact-head">
    <h2>Contact Brimwell Harbor</h2>
    <p>Make an Appointment</p>
  </div>
  <div class="abs field" style="left:403px;top:1385px;width:187px">Name</div>
  <div class="abs field" style="left:608px;top:1385px;width:188px">Email</div>
  <div class="abs field" style="left:403px;top:1434px;width:187px">Subject to discuss</div>
  <div class="abs field" style="left:608px;top:1434px;width:188px">mm/dd/yyyy
    <svg style="position:absolute;right:9px;top:10px" width="11" height="11" viewBox="0 0 11 11"><rect x="0.5" y="1.5" width="10" height="9" fill="none" stroke="#666"/><path d="M0.5 4h10M3 0v3M8 0v3" stroke="#666"/></svg>
  </div>
  <div class="abs field area" style="left:403px;top:1483px;width:393px">Message</div>
  <span class="abs btn btn-send">Send</span>
</section>

<section>
  <div class="abs testi" role="img" aria-label="Faint blue-tinted photo of a counselling session"></div>
  <svg class="abs quote-mark" width="40" height="30" viewBox="0 0 40 30"><path d="M2 28V17C2 8 6 3 14 1l1 3c-5 2-7 5-7 10h7v14zM23 28V17c0-9 4-14 12-16l1 3c-5 2-7 5-7 10h7v14z" fill="#fff"/></svg>
  <p class="abs testi-text">Sed pretium fermentum dui eget pharetra. Vivamus dictum eleifend turpis, nec congue nibh viverra nec. Pellentesque ut dapibus mi, vehicula fermentum ante. Proin rutrum nec ex ac egestas. Donec pretium, felis eget euismod pulvinar, leo dolor iaculis lacus, at pulvinar mi nibh sed elit.</p>
  <div class="abs testi-dots"><i></i><i class="on"></i><i></i></div>
  <div class="abs testi-photo" role="img" aria-label="Client portrait, woman in a white shirt holding a clipboard"></div>
  <div class="abs testi-name">Tomas Reyland</div>
  <div class="abs testi-role">Client</div>
</section>

<footer>
  <div class="abs foot-brand brand">
    <div class="brand-mark"></div>
    <div class="brand-name">Brimwell Harbor</div>
    <div class="brand-rule"></div>
    <div class="brand-tag">Renewal Aftercare</div>
  </div>
  <div class="abs social"><i></i><i></i><i></i><i></i><i></i></div>
  <div class="abs copy">Brimwell Harbor © 2019. All rights reserved.</div>
</footer>

</body>
</html>
```